Business Card Design

Design new business card using new logo attached and some details as old business card, which is also attached.

Industry/Entity Type

Business

```html
<!DOCTYPE html>
<html lang="en">
<head>
<meta charset="utf-8">
<title>DRW Business Card</title>
<link href="https://fonts.googleapis.com/css2?family=Libre+Baskerville:wght@400;700&family=Arimo:wght@400&display=swap" rel="stylesheet">
<style>
  :root {
    --navy: #1c1a7a;
    --grey: #8a8b8e;
    --grey-band: #8e8f93;
    --ink: #2a2a2a;
    --card: #ffffff;
    --backdrop: #e9e7e3;
  }
  html, body {
    margin: 0;
    width: 1200px;
    height: 900px;
    overflow: hidden;
    background: var(--backdrop);
  }
  .canvas {
    position: relative;
    width: 1200px;
    height: 900px;
  }
  .card {
    position: absolute;
    left: 180px;
    top: 210px;
    width: 840px;
    height: 480px;
    background: var(--card);
    box-shadow: 0 6px 24px rgba(0,0,0,0.12);
    overflow: hidden;
  }
  .band-grey {
    position: absolute;
    left: 0; right: 0;
    bottom: 70px;
    height: 18px;
    background: var(--grey-band);
  }
  .band-navy {
    position: absolute;
    left: 0; right: 0;
    bottom: 0;
    height: 70px;
    background: var(--navy);
  }
  .edge-tab {
    position: absolute;
    left: 0;
    top: 250px;
    width: 14px;
    height: 60px;
    background: var(--grey-band);
  }
  .brand {
    position: absolute;
    left: 52px;
    top: 52px;
    display: flex;
    align-items: center;
  }
  .brand-mark {
    width: 16px;
    height: 16px;
    background: var(--navy);
    margin-right: 10px;
  }
  .brand-name {
    font-family: "Arimo", sans-serif;
    font-weight: 400;
    font-size: 44px;
    line-height: 1;
    color: var(--navy);
  }
  .brand-divider {
    width: 1px;
    height: 84px;
    background: var(--grey);
    margin: 0 18px 0 20px;
  }
  .services {
    font-family: "Libre Baskerville", serif;
    color: var(--navy);
    font-size: 21px;
    line-height: 1.15;
    text-transform: uppercase;
    margin: 0;
    font-weight: 400;
  }
  .services-owner {
    font-family: "Libre Baskerville", serif;
    font-size: 11px;
    letter-spacing: 1.3px;
    color: var(--grey);
    text-transform: uppercase;
    margin-top: 6px;
  }
  .holder {
    position: absolute;
    left: 56px;
    top: 178px;
  }
  .holder-name {
    font-family: "Libre Baskerville", serif;
    font-weight: 700;
    font-size: 25px;
    color: var(--navy);
    margin: 0;
  }
  .holder-title {
    font-family: "Libre Baskerville", serif;
    font-size: 24px;
    color: var(--grey);
    margin-top: 6px;
  }
  .address {
    position: absolute;
    left: 56px;
    top: 290px;
    display: flex;
    gap: 10px;
    font-family: "Arimo", sans-serif;
    font-size: 20px;
    line-height: 1.25;
    color: var(--ink);
  }
  .address svg { margin-top: 3px; flex: none; }
  .contacts {
    position: absolute;
    right: 40px;
    top: 44px;
    list-style: none;
    margin: 0;
    padding: 0;
    font-family: "Arimo", sans-serif;
    font-size: 18px;
    line-height: 1.35;
    color: var(--ink);
  }
  .contacts li {
    display: flex;
    align-items: center;
    gap: 10px;
  }
  .contacts svg { flex: none; }
</style>
</head>
<body>
<div class="canvas">
  <div class="card">
    <div class="brand">
      <div class="brand-mark"></div>
      <div class="brand-name">DRW</div>
      <div class="brand-divider"></div>
      <div>
        <h1 class="services">Tax, Accounting &amp;<br>Advisory Services</h1>
        <div class="services-owner">Daniel R. Whitfield, CPA, PA</div>
      </div>
    </div>

    <div class="holder">
      <h2 class="holder-name">Daniel R. Whitfield</h2>
      <div class="holder-title">CPA,PA</div>
    </div>

    <div class="address">
      <svg width="16" height="16" viewBox="0 0 16 16" aria-hidden="true">
        <path d="M8 1 L15 7 H13 V15 H3 V7 H1 Z" fill="none" stroke="#1c1a7a" stroke-width="1.6"/>
        <rect x="6.5" y="10" width="3" height="5" fill="#1c1a7a"/>
      </svg>
      <div>240 Harbor Crest Ave.<br>Seabrook Bay, FL&nbsp; 32900</div>
    </div>

    <ul class="contacts">
      <li>
        <svg width="14" height="14" viewBox="0 0 14 14" aria-hidden="true"><path d="M3 1 L5.5 1 L6.3 4 L4.7 5.3 C5.6 7.2 6.8 8.4 8.7 9.3 L10 7.7 L13 8.5 V11 C13 12 12 13 11 13 C5.5 12.6 1.4 8.5 1 3 C1 2 2 1 3 1 Z" fill="#1c1a7a"/></svg>
        (555) 014-2290
      </li>
      <li>
        <svg width="14" height="14" viewBox="0 0 14 14" aria-hidden="true"><rect x="3" y="0.5" width="8" height="13" rx="1.5" fill="#1c1a7a"/><rect x="4.3" y="2" width="5.4" height="8" fill="#fff"/></svg>
        (555) 017-3845
      </li>
      <li>
        <svg width="14" height="14" viewBox="0 0 14 14" aria-hidden="true"><rect x="1" y="3" width="12" height="8.5" fill="#1c1a7a"/><path d="M1 3 L7 8 L13 3" fill="none" stroke="#fff" stroke-width="1"/></svg>
        dan@drwcpa.example
      </li>
      <li>
        <svg width="14" height="14" viewBox="0 0 14 14" aria-hidden="true"><circle cx="7" cy="7" r="6" fill="#1c1a7a"/><path d="M1 7 H13 M7 1 C4 4 4 10 7 13 M7 1 C10 4 10 10 7 13" fill="none" stroke="#fff" stroke-width="0.9"/></svg>
        www.drwcpa.example
      </li>
    </ul>

    <div class="edge-tab"></div>
    <div class="band-grey"></div>
    <div class="band-navy"></div>
  </div>
</div>
</body>
</html>
```